Health and Wellness Company Business Card

I need a business card design that is clean and uses modern minimalist style. The design should incorporate our logo (see attached). I would also like to use embossing on the cards so that they also have a great feel. I am open to the card using one or more colors, and these do not have to correspond to the colors in the concept paper. The card can either be one-sided or use both sides of the card.The logo uses the Avenir font.

I will need the file designed in Adobe CS and compatible with CS5.5 (Illustrator preferable) and I'll need the working file (for example: .ai) once the project is complete so that I can change the names/contact info/etc for each variation of the card.

This needs to be a memorable card for the recipient. They should think: "This is a great business card" either because of its simplicity or embossing effects or use of color.

Target Market(s)

The audience for our company has two main groups: people who pay for healthcare (insurers, companies, researcher companies) and people with chronic health conditions who are the consumers of our services and resources.

Industry/Entity Type

Business

Requirements
Must have
• Essential components of the card include: Company logo, contact Name (Mark Tolley), phone number (5808127346), email address (mtolley@brenquora.com), slogan/tagline that consists of ~30-40 characters (Use Lorem Ipsum)
Nice to have
• These fall just slightly short of "must have" to allow for design flexibility: Embossing or spot varnish effects and a splash of color
Should not have
• Designs with these components will not be successful: flashy or showy designs that are not professional in appearance, and lots of different colors

```html
<!DOCTYPE html>
<html lang="en">
<head>
<meta charset="utf-8">
<title>Brenquora Business Card</title>
<link rel="stylesheet" href="https://fonts.googleapis.com/css2?family=Mulish:wght@300;400&display=swap">
<style>
  :root {
    --backdrop: #e6e6e8;
    --card: #ffffff;
    --brand-grey: #77758a;
    --ink-soft: #6f6e7c;
    --ink-text: #5c5b68;
    --accent-teal: #2f4f4f;
    --rule: #3d5a5a;
  }
  * { box-sizing: border-box; margin: 0; padding: 0; }
  html, body {
    width: 1200px;
    height: 840px;
    overflow: hidden;
    background: var(--backdrop);
    font-family: "Mulish", sans-serif;
  }
  .card-set {
    position: relative;
    width: 1200px;
    height: 840px;
  }
  .card {
    position: absolute;
    top: 157px;
    width: 300px;
    height: 525px;
    background: var(--card);
    box-shadow: 0 6px 18px rgba(0,0,0,0.12);
    overflow: hidden;
  }
  .card--front { left: 240px; }
  .card--back { left: 660px; }

  /* Front */
  .brand {
    position: absolute;
    top: 48px;
    left: 0;
    width: 100%;
    display: flex;
    justify-content: center;
    align-items: center;
    gap: 12px;
  }
  .brand__name {
    font-weight: 400;
    font-size: 17px;
    letter-spacing: 6px;
    color: var(--brand-grey);
    text-transform: uppercase;
  }
  .brand__square {
    width: 26px;
    height: 26px;
    border-radius: 5px;
    background: var(--brand-grey);
  }
  .holder-name {
    position: absolute;
    top: 112px;
    left: 0;
    width: 100%;
    text-align: center;
    font-weight: 300;
    font-size: 27px;
    letter-spacing: 1px;
    color: var(--ink-soft);
  }
  .name-rule {
    position: absolute;
    top: 150px;
    left: 30px;
    width: 270px;
    height: 60px;
  }
  .contact {
    position: absolute;
    top: 218px;
    left: 40px;
    font-size: 12.5px;
    line-height: 19px;
    color: var(--ink-text);
  }
  .contact__row { display: flex; gap: 10px; }
  .contact__label { width: 44px; }
  .website {
    position: absolute;
    top: 272px;
    left: 40px;
    font-size: 12.5px;
    color: var(--ink-text);
  }

  /* Back */
  .brand-field {
    position: absolute;
    top: 0;
    right: 0;
    width: 210px;
    height: 175px;
    background: linear-gradient(200deg, var(--brand-grey) 0%, #9c9aab 70%, rgba(255,255,255,0) 100%);
  }
  .tagline-frame {
    position: absolute;
    top: 190px;
    left: 20px;
    width: 280px;
    height: 160px;
  }
  .tagline {
    position: absolute;
    top: 240px;
    left: 58px;
    font-weight: 400;
    font-size: 30px;
    line-height: 34px;
    letter-spacing: 0.5px;
    color: var(--ink-soft);
    text-transform: uppercase;
  }
</style>
</head>
<body>
<main class="card-set">

  <section class="card card--front" aria-label="Card front">
    <div class="brand">
      <span class="brand__name">Brenquora</span>
      <span class="brand__square" aria-hidden="true"></span>
    </div>
    <h1 class="holder-name">MARK TOLLEY</h1>
    <svg class="name-rule" viewBox="0 0 270 60" aria-hidden="true">
      <rect x="0" y="0" width="9" height="8" rx="2" fill="var(--accent-teal)"/>
      <path d="M4 8 V44 Q4 52 12 52 H270" fill="none" stroke="var(--rule)" stroke-width="1"/>
    </svg>
    <div class="contact">
      <div class="contact__row"><span class="contact__label">Phone:</span><span>5808127346</span></div>
      <div class="contact__row"><span class="contact__label">Email:</span><span>mtolley@brenquora.com</span></div>
    </div>
    <div class="website">www.brenquora.com</div>
  </section>

  <section class="card card--back" aria-label="Card back">
    <div class="brand-field" role="img" aria-label="Large brand mark decoration area"></div>
    <svg class="tagline-frame" viewBox="0 0 280 160" aria-hidden="true">
      <path d="M280 4 H38 Q24 4 24 18 V140" fill="none" stroke="var(--brand-grey)" stroke-width="6"/>
      <rect x="14" y="136" width="20" height="20" rx="5" fill="var(--brand-grey)"/>
    </svg>
    <p class="tagline">Your tagline<br>goes here</p>
  </section>

</main>
</body>
</html>
```